Bottle label for a drinking or cocktail vinegar called Amber Hollow Shrub

We need a label for a square bottle that measures 2.75 inches on a side and is 6.75 inches tall. The volume is 16.9oz/500mL. The corners are rounded. A photo has been uploaded. The label should be one piece that wraps around 2-3 sides rather than separate front and back labels. The maximum height of the label can be 3.25 inches.

The company name is Amber Hollow Vinegar Works. The product line is called Amber Hollow Shrub.

The product is what is called a drinking vinegar, or sometimes cocktail vinegar, the kind of vinegar that is added to cocktails or used to make a beverage. Drinking vinegar, also known as a shrub, is vinegar and sugar mixed with fruit. The resulting elixir is tart and sweet, and is used as an alternative to lemon or lime in many drinks where it introduces an acid but with a different fruit flavor. A simple, non-alcoholic beverage can be made by adding shrub to sparkling water over ice.

Amber Hollow Shrubs are handcrafted in small batches in a small town called Deep River which is on the bank of the Connecticut River in New England. Some of the flavors include Pomegranate, Pineapple/Basil, Cherry, Fennel/Apple, and Elderberry. New flavors are added and old flavors go away, such is the nature of small batch production.

Some key words that may be useful are: artisan, small batch, handcrafted, cocktail vinegar, drinking vinegar, shrub, seasonal, natural, whole fruit.

Target Market(s)

The target audience is 25-40 year olds that drink cocktails rather than beer.

Requirements
Must have
• In addition to usual label contents (name, ingredients, volume, company info, etc.), There should be space for a hand written Batch number, description of a shrub, sample recipes, “Shake before using”.
Should not have
• nutrition labeling is not needed

```html
<!DOCTYPE html>
<html lang="en">
<head>
<meta charset="utf-8">
<title>Amber Hollow Shrub – Wrap Label</title>
<link rel="stylesheet" href="https://fonts.googleapis.com/css2?family=Quicksand:wght@500;600;700&family=Mulish:wght@600;700&family=Josefin+Slab:wght@600;700&family=Courgette&display=swap">
<style>
  :root{
    --backdrop:#efece6;
    --kraft:#dccca6;
    --kraft-dark:#cdbb91;
    --gold:#b3952c;
    --gold-line:#b88f2c;
    --navy:#1c2a45;
    --cream:#f3ecd2;
    --flavor-pink:#c8185a;
    --white:#ffffff;
    --meadow-light:#d3c58a;
    --meadow-dark:#8f8a4a;
  }
  *{box-sizing:border-box;margin:0;padding:0}
  html,body{width:1200px;height:1124px;overflow:hidden;background:var(--backdrop)}
  .canvas{position:relative;width:1200px;height:1124px}
  .label{
    position:absolute;left:75px;top:227px;width:1049px;height:669px;
    background:radial-gradient(ellipse at 40% 40%, var(--kraft) 0%, var(--kraft-dark) 140%);
    font-family:"Mulish",sans-serif;color:var(--navy);
  }
  .panel{position:absolute;top:0;height:100%}
  .panel--left{left:0;width:388px}
  .panel--front{left:388px;width:274px;background:var(--gold);overflow:hidden}
  .panel--right{left:662px;width:387px}

  .info-frame{
    position:absolute;top:64px;width:221px;height:278px;
    border:2px solid var(--gold-line);border-radius:6px;
    padding:24px 14px 0;text-align:center;
  }
  .panel--left .info-frame{left:76px}
  .panel--right .info-frame{left:102px}
  .info-title{
    font-family:"Quicksand",sans-serif;font-weight:700;font-size:25px;
    letter-spacing:.5px;text-transform:uppercase;margin-bottom:12px;
  }
  .info-body{font-size:12.4px;line-height:15.6px;font-weight:600}

  .wave-band{
    position:absolute;top:372px;left:0;width:100%;height:98px;
    background:linear-gradient(180deg,rgba(28,42,69,0) 0%,rgba(28,42,69,.18) 50%,rgba(28,42,69,0) 100%);
  }

  .recipe{position:absolute;left:108px;top:482px;width:245px}
  .recipe-title{font-family:"Quicksand",sans-serif;font-weight:700;font-size:25px;text-transform:uppercase;line-height:28px}
  .recipe-body{font-size:12.4px;line-height:15.6px;font-weight:600}

  .brand{
    position:absolute;left:16px;top:46px;width:242px;
    font-family:"Quicksand",sans-serif;font-weight:700;color:var(--navy);
    text-transform:uppercase;line-height:1;white-space:nowrap;
  }
  .brand-line{display:block;font-size:52px;letter-spacing:0}
  .brand-line--small{font-size:28px;text-align:right;margin-top:4px;letter-spacing:1px}
  .flavor-script{
    position:absolute;left:0;top:268px;width:100%;text-align:center;
    font-family:"Courgette",cursive;font-size:36px;color:var(--navy);transform:rotate(-3deg);
  }
  .shake-note{
    position:absolute;left:0;top:360px;width:100%;text-align:center;
    font-family:"Quicksand",sans-serif;font-weight:600;color:var(--cream);
    font-size:12.5px;letter-spacing:.5px;text-transform:uppercase;
  }
  .shake-note strong{display:block;font-size:17px;letter-spacing:2px;font-weight:700;margin-top:1px}
  .landscape{
    position:absolute;left:0;top:398px;width:100%;height:74px;
    background:linear-gradient(180deg,var(--meadow-light) 0%,#c2b674 45%,var(--meadow-dark) 100%);
  }
  .info-box{
    position:absolute;left:14px;top:480px;width:240px;height:168px;
    background:var(--white);border:1.5px solid var(--navy);
  }
  .info-box > div{border-bottom:1.5px solid var(--navy)}
  .batch-row{height:41px;font-family:"Josefin Slab",serif;font-weight:700;font-size:19px;letter-spacing:2px;text-align:center;line-height:46px}
  .batch-blank{height:31px}
  .spec-row{height:42px;display:flex}
  .spec-cell{padding:3px 4px;font-family:"Josefin Slab",serif;font-weight:700;font-size:11.5px;letter-spacing:1px;text-transform:uppercase}
  .spec-cell--volume{width:92px;border-right:1.5px solid var(--navy)}
  .spec-value{font-family:"Mulish",sans-serif;text-transform:none;letter-spacing:0;font-size:11px;font-weight:600;display:block;margin-top:3px}
  .spec-value--flavor{color:var(--flavor-pink);font-size:17px;margin-top:0}
  .info-box > .bottler{border-bottom:none;padding:3px 6px}
  .bottler-name{font-family:"Mulish",sans-serif;font-size:15px;font-weight:600;text-align:center;margin-top:6px;text-transform:none;letter-spacing:0}
  .tagline{
    position:absolute;left:0;top:652px;width:100%;text-align:center;
    font-family:"Josefin Slab",serif;font-weight:700;font-size:8.5px;letter-spacing:2px;color:var(--navy);text-transform:uppercase;
  }
</style>
</head>
<body>
<main class="canvas">
  <section class="label">
    <div class="wave-band" role="img" aria-label="Band of fine wavy river lines across the label"></div>

    <div class="panel panel--left">
      <div class="info-frame">
        <h2 class="info-title">Ingredients</h2>
        <p class="info-body">Nulla at nulla justo, eget luctus tortor. Nulla facilisi. Duis aliquet egestas purus in blandit. Curabitur vulputate, ligula lacinia scelerisque tempor, lacus lacus ornare ante, ac egestas est urna sit amet arcu. Class aptent taciti sociosqu ad litora torquent per conubia nostra, per inceptos himenaeos. Sed molestie augue sit amet leo consequat posuere.</p>
      </div>
    </div>

    <div class="panel panel--front">
      <h1 class="brand">
        <span class="brand-line">Amber</span>
        <span class="brand-line">Hollow</span>
        <span class="brand-line brand-line--small">Shrub</span>
      </h1>
      <p class="flavor-script">Pomegranate</p>
      <p class="shake-note">Shake before using<strong>Vinegar</strong></p>
      <div class="landscape" role="img" aria-label="Illustration of a river winding through meadows and hills"></div>
      <div class="info-box">
        <div class="batch-row">BATCH №</div>
        <div class="batch-blank"></div>
        <div class="spec-row">
          <div class="spec-cell spec-cell--volume">Volume:<span class="spec-value">16.9oz/500mL</span></div>
          <div class="spec-cell">Flavor:<span class="spec-value spec-value--flavor">Pomegranate</span></div>
        </div>
        <div class="spec-cell bottler">Bottled by:<div class="bottler-name">Amber Hollow Vinegar Works</div></div>
      </div>
      <p class="tagline">Handcrafted | Quality | Shrub</p>
    </div>

    <div class="panel panel--right">
      <div class="info-frame">
        <h2 class="info-title">About Us</h2>
        <p class="info-body">Nulla at nulla justo, eget luctus tortor. Nulla facilisi. Duis aliquet egestas purus in blandit. Curabitur vulputate, ligula lacinia scelerisque tempor, lacus lacus ornare ante, ac egestas est urna sit amet arcu. Class aptent taciti sociosqu ad litora torquent per conubia nostra, per inceptos himenaeos. Sed molestie augue sit amet leo consequat posuere.</p>
      </div>
      <div class="recipe">
        <h2 class="recipe-title">Recipe:</h2>
        <p class="recipe-body">Nulla at nulla justo, eget luctus tortor. Nulla facilisi. Duis aliquet egestas purus in blandit. Curabitur vulputate, ligula lacinia scelerisque tempor, lacus lacus ornare ante, ac egestas est urna sit ametarcu. Class aptent taciti sociosqu ad litora torquent per conubia nostra, per inceptos himenaeos. Sed molestie augue sit amet leo consequatposuere.</p>
      </div>
    </div>
  </section>
</main>
</body>
</html>
```